Website Design Project for Beauty & Wellness Professionals

As background information, I have a website that is focused on Beauty & Wellness Professionals:
- Job Search (www.trilhavelora.com)
- Business Classifieds (negocios.trilhavelora.com)
- Freelancer Classifieds (freelancer.trilhavelora.com)
- Course Reviews (cursos.trilhavelora.com)

All those websites use standard templates.

I need a DESIGN for the HOME PAGE (no coding) of the Website Platform that consolidates the four platforms under the same design.

Website designs that we like:
- quovenda.com
- mirtelpeek.com

Target Market(s)

Brazilian Professionals from Beauty & Wellness sector

Industry/Entity Type

Business

Requirements
Must have
• Website designs that we like:
- quovenda.com
- mirtelpeek.com

```html
<!DOCTYPE html>
<html lang="en">
<head>
<meta charset="utf-8">
<title>Trilha Velora</title>
<link href="https://fonts.googleapis.com/css2?family=Open+Sans:wght@400;600;700;800&display=swap" rel="stylesheet">
<style>
:root{
  --green:#8cbf8f;
  --green-dark:#6fa874;
  --brown:#8a4f26;
  --ink:#333;
  --muted:#777;
  --rule:#dcdcdc;
  --footer:#2b2b2b;
  --paper:#fff;
}
*{box-sizing:border-box;margin:0;padding:0}
html,body{width:766px;height:1200px;overflow:hidden;background:var(--paper);font-family:"Open Sans",Arial,sans-serif;color:var(--ink)}
.page{position:relative;width:766px;height:1200px}
.site-header{height:50px;display:flex;align-items:center;justify-content:space-between;padding-left:90px;padding-right:50px}
.brand{display:flex;align-items:center;gap:8px;font-size:20px;font-weight:600;color:var(--green-dark)}
.brand-mark{width:22px;height:22px;border-radius:50%;background:var(--green)}
.main-nav{display:flex;height:50px}
.main-nav a{display:flex;align-items:center;padding:0 13px;font-size:10px;font-weight:600;color:var(--muted);text-decoration:none;text-transform:uppercase}
.main-nav a.active{background:var(--green);color:#fff}
.hero{position:relative;height:280px;background:linear-gradient(100deg,#6f9fa6 0%,#a7c9cc 30%,#d8b7a1 55%,#7fa6a4 100%)}
.booking{position:absolute;right:50px;top:0;width:210px;height:255px;background:rgba(138,79,38,.92);padding:20px 14px}
.booking h2{color:#fff;font-size:14px;font-weight:700;text-align:center;white-space:nowrap;margin-bottom:16px}
.field{display:flex;align-items:center;margin-bottom:12px}
.field span{width:52px;color:#f3dfcf;font-size:10px}
.field i{flex:1;height:22px;background:#fff}
.submit{display:block;margin:6px 0 0 52px;width:70px;height:24px;background:var(--green);color:#fff;font-size:11px;font-weight:700;text-align:center;line-height:24px}
.welcome{display:flex;gap:24px;padding:28px 90px 0;height:245px}
.welcome-photo{flex:0 0 170px;width:170px;height:170px;border:1px solid var(--rule);padding:5px}
.welcome-photo div{width:100%;height:100%;background:linear-gradient(135deg,#e9cdb8,#c89a7d)}
.welcome h1{font-size:30px;font-weight:800;letter-spacing:1px}
.welcome h3{font-size:15px;font-weight:800;text-transform:uppercase;line-height:1.2;margin:4px 0 8px}
.welcome p{font-size:10px;line-height:1.5;color:var(--muted)}
.columns{display:flex;gap:30px;padding:20px 90px 0;height:330px;border-top:1px solid var(--rule)}
.col{flex:1}
.col h2{font-size:17px;font-weight:800;margin-bottom:12px}
.col-photo{height:100px;margin-bottom:10px}
.col p{font-size:9.5px;line-height:1.55;color:var(--muted)}
.col ul{list-style:none}
.col li{font-size:9px;line-height:1.2;color:var(--muted);border-bottom:1px solid #eee;padding:1px 0 1px 12px;position:relative}
.col li::before{content:"";position:absolute;left:2px;top:5px;width:4px;height:4px;background:var(--brown)}
.mission-strip{display:flex;gap:4px;height:70px;margin-bottom:8px}
.mission-strip div{flex:1}
.col h4{font-size:9.5px;font-weight:700;color:var(--ink)}
.more{display:inline-block;margin-top:12px;background:var(--brown);color:#fff;font-size:10px;font-weight:700;padding:5px 14px}
.links{padding:16px 90px 0;height:213px;border-top:1px solid var(--rule)}
.links h2{font-size:15px;font-weight:700;color:var(--muted);margin-bottom:12px}
.cards{display:flex;gap:18px}
.card{flex:1;text-align:center}
.card-box{height:125px;border-radius:8px;overflow:hidden;background:#555;display:flex;flex-direction:column}
.card-title{height:42px;color:#fff;font-size:12px;font-weight:800;display:flex;align-items:center;justify-content:center;line-height:1.1;text-transform:uppercase}
.card-photo{flex:1}
.card a{display:block;margin-top:8px;font-size:9px;font-weight:700;color:var(--ink);text-decoration:underline}
.site-footer{position:absolute;left:0;right:0;bottom:0;height:82px;background:var(--footer)}
.footer-bar{display:flex;align-items:center;justify-content:space-between;height:50px;padding:0 50px}
.footer-nav{display:flex;gap:14px}
.footer-nav a{color:#ccc;font-size:9px;text-decoration:none}
.social{display:flex;gap:6px}
.social i{width:18px;height:18px;border-radius:50%;background:#777}
.copyright{padding:4px 50px;font-size:8px;color:#888}
</style>
</head>
<body>
<div class="page">
  <header class="site-header">
    <div class="brand"><span class="brand-mark"></span>Trilha Velora</div>
    <nav class="main-nav">
      <a class="active" href="#">Home</a><a href="#">About us</a><a href="#">Services</a><a href="#">Gallery</a><a href="#">Contact us</a>
    </nav>
  </header>

  <section class="hero" role="img" aria-label="Woman relaxing at a spa with a pink flower, soft teal background">
    <form class="booking">
      <h2>BOOK YOUR APPOINTMENT</h2>
      <label class="field"><span>Name:</span><i></i></label>
      <label class="field"><span>Email:</span><i></i></label>
      <label class="field"><span>Phone:</span><i></i></label>
      <label class="field"><span>Date:</span><i style="height:44px"></i></label>
      <span class="submit">SUBMIT</span>
    </form>
  </section>

  <section class="welcome">
    <div class="welcome-photo"><div role="img" aria-label="Beauty portrait with makeup"></div></div>
    <div>
      <h1>WELCOME !</h1>
      <h3>In pede mi, aliquet sit amet, euismod in,auctor ut, ligula</h3>
      <p>Nulla id tempus quam. Integer augue eros, varius sed magna at, pretium feugiat enim. Curabitur vel dictum orci, et tempor lectus. Fusce quis risus nec turpis ultricies tempor vitae non urna. Aliquam erat volutpat.</p>
    </div>
  </section>

  <section class="columns">
    <div class="col">
      <h2>WHY CHOOSE US</h2>
      <div class="col-photo" role="img" aria-label="Spa massage treatment" style="background:linear-gradient(135deg,#f1ece6,#cdb7a4)"></div>
      <p>Ut finibus tellus eu lacinia aliquet. Nam venenatis ultrices tortor ac fermentum. Sed non augue mi, vitae mollis nisl laoreet.</p>
      <span class="more">More</span>
    </div>
    <div class="col">
      <h2>SERVICES</h2>
      <div class="col-photo" role="img" aria-label="Facial beauty treatment" style="background:linear-gradient(135deg,#f4e6dc,#d8ae92)"></div>
      <ul>
        <li>Facial skin care</li><li>Relaxing body massage</li><li>Hair cut styling</li><li>Manicure and pedicure</li><li>Makeup for events</li><li>Eyebrow design studio</li><li>Aesthetic wellness therapy</li>
      </ul>
      <span class="more">More</span>
    </div>
    <div class="col">
      <h2>OUR MISSION</h2>
      <div class="mission-strip" role="img" aria-label="Strip of wellness photos: candles, stones, cosmetics">
        <div style="background:#b07a4e"></div><div style="background:#d9c2a8"></div><div style="background:#7a5a3f"></div><div style="background:#c49b7b"></div>
      </div>
      <h4>Our commitment to professionals</h4>
      <p>Connecting beauty talent with salons, clinics and spas across Brazil every day.</p>
      <h4>Trusted opportunities for everyone</h4>
      <p>We review every listing so candidates and employers can meet with confidence.</p>
      <span class="more">More</span>
    </div>
  </section>

  <section class="links">
    <h2>OUR LINKS:</h2>
    <div class="cards">
      <div class="card"><div class="card-box"><div class="card-title">Job<br>Search</div><div class="card-photo" role="img" aria-label="Beauty professional at work" style="background:linear-gradient(#d9b79c,#a7785a)"></div></div><a href="#">CLICK HERE</a></div>
      <div class="card"><div class="card-box"><div class="card-title">Business<br>Classifieds</div><div class="card-photo" role="img" aria-label="Salon business scene" style="background:linear-gradient(#cfd8d6,#8aa6a3)"></div></div><a href="#">CLICK HERE</a></div>
      <div class="card"><div class="card-box"><div class="card-title">Freelancer<br>Classifieds</div><div class="card-photo" role="img" aria-label="Freelance beautician" style="background:linear-gradient(#e6cdb9,#b58b6c)"></div></div><a href="#">CLICK HERE</a></div>
      <div class="card"><div class="card-box"><div class="card-title">Course<br>Reviews</div><div class="card-photo" role="img" aria-label="Beauty course student" style="background:linear-gradient(#c6b2a2,#8e6c58)"></div></div><a href="#">CLICK HERE</a></div>
    </div>
  </section>

  <footer class="site-footer">
    <div class="footer-bar">
      <nav class="footer-nav"><a href="#">Home</a><a href="#">About us</a><a href="#">Services</a><a href="#">Gallery</a><a href="#">Blog</a><a href="#">Contact us</a></nav>
      <div class="social"><i></i><i></i><i></i><i></i></div>
    </div>
    <p class="copyright">Copyright 2014 trilhavelora.com All Rights Reserved</p>
  </footer>
</div>
</body>
</html>
```